Billboard design - consider what a billboard is

Design a billboard using my logo - Billboard is 6m x 3m
A Billboard is advertising for my company that is on a big sign.

Has to be clean and easy to read, and ideally highlights that we are Residential and Commercial builders.

Keep it clean and easy to read

The contact number for the board is

022 583 7092
www.harbourframeworks.co.nz
info@harbourframeworks.co.nz

Doesnt have to have all contact details if it doesnt fit

Has to catch peoples attention to contact us if they need a builder

Can you please change the sign to be all white writing, with black background ?
Updates

Please consider what a billboard is...

The design needs to be suitable for a billboard..

Target Market(s)

people driving past

Industry/Entity Type

Construction

Logo Text

Wellington Builder, website email address, contact number

Colors
0054AA
0677BA
7BADD7
CADEEF
E8F1F8

Requirements
Must have
• Easy to read
Nice to have
• easy to read, can clearly see contact details

```html
<!DOCTYPE html>
<html lang="en">
<head>
<meta charset="utf-8">
<title>Harbour Frameworks Billboard</title>
<link rel="stylesheet" href="https://fonts.googleapis.com/css2?family=Arimo:wght@700&family=Questrial&display=swap">
<style>
  :root {
    --board-navy: #0a0f9c;
    --accent-sky: #0ab2f2;
    --text-white: #ffffff;
    --page-bg: #ffffff;
  }
  * { margin: 0; padding: 0; box-sizing: border-box; }
  html, body {
    width: 1200px;
    height: 919px;
    overflow: hidden;
    background: var(--page-bg);
  }
  .billboard {
    position: absolute;
    left: 0;
    top: 160px;
    width: 1200px;
    height: 600px;
    background: var(--board-navy);
    overflow: hidden;
  }
  .brand-mark {
    position: absolute;
    left: 62px;
    top: 40px;
    width: 110px;
    height: 110px;
    background: var(--accent-sky);
  }
  .brand-name {
    position: absolute;
    left: 232px;
    top: 22px;
    font-family: "Arimo", Arial, sans-serif;
    font-weight: 700;
    font-size: 112px;
    line-height: 118px;
    letter-spacing: -2px;
    color: var(--accent-sky);
  }
  .contact-list {
    position: absolute;
    left: 236px;
    top: 322px;
    list-style: none;
    font-family: "Questrial", "Century Gothic", sans-serif;
    color: var(--text-white);
  }
  .contact-item {
    display: flex;
    align-items: center;
    gap: 18px;
  }
  .contact-item svg { flex: none; }
  .contact-phone {
    font-size: 62px;
    color: var(--accent-sky);
    height: 90px;
    margin-bottom: 8px;
  }
  .contact-web, .contact-email {
    font-size: 38px;
    height: 74px;
  }
  .hl { color: var(--accent-sky); }
</style>
</head>
<body>
  <section class="billboard">
    <div class="brand-mark"></div>
    <h1 class="brand-name">Harbour<br>Frameworks</h1>
    <ul class="contact-list">
      <li class="contact-item contact-phone">
        <svg width="44" height="58" viewBox="0 0 44 58" aria-hidden="true">
          <path d="M12 4 L20 16 L14 22 Q16 34 26 42 L32 36 L42 46 L34 54 Q8 48 4 14 Z" fill="none" stroke="#ffffff" stroke-width="5" stroke-linejoin="round"/>
        </svg>
        <span>022 583 7092</span>
      </li>
      <li class="contact-item contact-web">
        <svg width="56" height="56" viewBox="0 0 56 56" aria-hidden="true">
          <g fill="none" stroke="#ffffff" stroke-width="3.5">
            <circle cx="28" cy="28" r="25"/>
            <ellipse cx="28" cy="28" rx="11" ry="25"/>
            <line x1="3" y1="28" x2="53" y2="28"/>
            <path d="M7 15 H49 M7 41 H49"/>
          </g>
        </svg>
        <span>www.<span class="hl">harbourframeworks</span>.co.nz</span>
      </li>
      <li class="contact-item contact-email">
        <svg width="56" height="40" viewBox="0 0 56 40" aria-hidden="true">
          <g fill="none" stroke="#ffffff" stroke-width="3.5" stroke-linejoin="round">
            <rect x="2" y="2" width="52" height="36"/>
            <path d="M2 2 L28 24 L54 2 M2 38 L21 18 M54 38 L35 18"/>
          </g>
        </svg>
        <span>info@<span class="hl">harbourframeworks</span>.co.nz</span>
      </li>
    </ul>
  </section>
</body>
</html>
```